Barbados hotel and property development company needs new corporate PowerPoint deck design

We need a new corporate PowerPoint deck for harbourline holdings - a Barbados based company who operate and develop a hotel called the heron (https://www.theheronvilla.example/)
We need a professional deck we can use across our organisation to interact with investors and property buyers. This deck needs placeholder / slide types to present financial and text tables, s well as graphs and charts

Target Market(s)

Investors, property buyers and corporate audience

Industry/Entity Type

Hospitality and tourism

Colors
0054AA
0677BA
7BADD7
CADEEF
E8F1F8
0094D4
00A9DD
6FCCEA
C7EBF8
E9F6FB

Requirements
Must have
• Follow our blue based design and graphic principles per or website
Nice to have
• We’ve got lots of high res pictures of our beach, rooms and property on the website. We would like to use these as page breaks and divider slides in our deck

```html
<!DOCTYPE html>
<html lang="en">
<head>
<meta charset="utf-8">
<title>The Heron – Corporate Presentation Slides</title>
<link href="https://fonts.googleapis.com/css2?family=Roboto:wght@300;400;500;700;900&family=Montserrat:wght@400;600;700&display=swap" rel="stylesheet">
<style>
:root{
  --blue:#0f5a94;
  --blue-deep:#0b4a7c;
  --orange:#f47b20;
  --sky:#6fccea;
  --sky-light:#c7ebf8;
  --ink:#27313b;
  --grey:#8b949d;
  --line:#dfe3e7;
  --page:#d7d8da;
  --white:#ffffff;
}
*{margin:0;padding:0;box-sizing:border-box}
html,body{width:905px;height:1200px;overflow:hidden;background:var(--page)}
body{position:relative;font-family:Montserrat,sans-serif}
.slide{position:absolute;width:270px;height:152px;background:var(--white);overflow:hidden;box-shadow:0 2px 4px rgba(0,0,0,.22)}
.slide>*{position:absolute}
.col1{left:37px}.col2{left:320px}.col3{left:602px}
.row1{top:37px}.row2{top:200px}.row3{top:363px}.row4{top:526px}.row5{top:689px}.row6{top:852px}.row7{top:1015px}
.brand{right:8px;top:8px;color:var(--blue);font:500 7.5px/1 Roboto,sans-serif;white-space:nowrap}
.page-no{right:8px;bottom:6px;width:9px;height:9px;border:1px solid var(--sky);border-radius:50%;font:3px/7px Montserrat,sans-serif;text-align:center;color:var(--blue)}
.heading{font:500 9.5px/1 Roboto,sans-serif;color:var(--blue);white-space:nowrap}
.rule{height:1.5px;width:16px;background:var(--orange)}
.copy{font:3.1px/1.4 Montserrat,sans-serif;color:var(--grey)}
.copy-white{font:3.1px/1.4 Montserrat,sans-serif;color:var(--white)}
.label{font:600 4.2px/1.1 Montserrat,sans-serif;color:var(--blue)}
.photo{background:linear-gradient(135deg,#9fc3d8,#5b8aa6 55%,#c9b79a)}
.photo.warm{background:linear-gradient(135deg,#c8a27e,#7d5a44 60%,#3f3a36)}
.photo.green{background:linear-gradient(160deg,#9cc4e0,#7a9e58 55%,#4e6c34)}
.photo.pool{background:linear-gradient(180deg,#bcd9ef 0%,#8fb9d6 40%,#3ab3cf 70%,#c7b59a 100%)}
.sq{width:7px;height:7px;background:var(--orange)}
.sq.blue{background:var(--blue)}
.divider-title{font:400 13px/1.05 Roboto,sans-serif;color:var(--white)}
.divider-title b{font-weight:700}
.num{font:700 5px Montserrat,sans-serif;color:var(--blue)}
.dot{width:4px;height:4px;border-radius:50%;background:var(--ink)}
.icon-box{width:19px;height:19px;display:flex;align-items:center;justify-content:center}
.icon-box svg{width:11px;height:11px}
.bg-blue{background:var(--blue)}.bg-orange{background:var(--orange)}
.center{text-align:center}
</style>
</head>
<body>

<!-- 1 Cover -->
<section class="slide col1 row1">
  <div class="sq" style="left:6px;top:5px"></div>
  <div style="left:17px;top:26px;color:var(--blue);font:500 15px/1 Roboto,sans-serif">The Heron</div>
  <div style="left:17px;top:80px;font:400 6.5px Roboto,sans-serif;color:var(--orange)">PRESENTATION</div>
  <div style="left:17px;top:89px;font:900 17px/1 Roboto,sans-serif;color:var(--blue)">BUSINESS</div>
  <div style="left:17px;top:108px;font:700 12px/1 Roboto,sans-serif;color:var(--orange)">MARKETING</div>
  <div class="dot" style="left:17px;top:138px;width:2.5px;height:2.5px"></div>
  <div class="dot" style="left:22px;top:138px;width:2.5px;height:2.5px;background:var(--orange)"></div>
  <div class="dot" style="left:27px;top:138px;width:2.5px;height:2.5px"></div>
  <div class="photo pool" role="img" aria-label="Villa terrace with sun loungers beside an infinity pool and the sea" style="left:113px;top:0;width:157px;height:123px"></div>
  <div class="bg-blue" style="left:113px;top:123px;width:157px;height:29px"></div>
  <div style="left:113px;top:134px;width:157px;text-align:center;font:400 4.5px Montserrat,sans-serif;letter-spacing:1px;color:#fff">www.theheronvilla.example</div>
</section>

<!-- 2 Agenda -->
<section class="slide col2 row1">
  <div class="brand">The Heron</div>
  <div class="heading" style="left:42px;top:18px;font-size:11px">Agenda</div>
  <div class="bg-blue" style="left:0;top:123px;width:64px;height:29px"></div>
  <div class="photo green" role="img" aria-label="Couple walking together on a sunny resort terrace" style="left:21px;top:37px;width:90px;height:90px"></div>
  <div style="left:122px;top:39px;width:110px">
    <div class="label">1. Lorem ipsum</div><div class="copy" style="margin:1px 0 8px 6px">Lorem ipsum dolor sit amet, consectetuer adipiscing elit, sed diam nonummy nibh euismod</div>
    <div class="label">2. Lorem ipsum</div><div class="copy" style="margin:1px 0 8px 6px">Lorem ipsum dolor sit amet, consectetuer adipiscing elit, sed diam nonummy nibh euismod</div>
    <div class="label">3. Lorem ipsum</div><div class="copy" style="margin:1px 0 8px 6px">Lorem ipsum dolor sit amet, consectetuer adipiscing elit, sed diam nonummy nibh euismod</div>
    <div class="label">4. Lorem ipsum</div><div class="copy" style="margin:1px 0 0 6px">Lorem ipsum dolor sit amet, consectetuer adipiscing elit, sed diam nonummy nibh euismod</div>
  </div>
  <div class="page-no">2</div>
</section>

<!-- 3 Subject title -->
<section class="slide col3 row1">
  <div class="bg-orange" style="left:0;top:0;width:130px;height:8px"></div>
  <div class="brand">The Heron</div>
  <div class="heading" style="left:13px;top:22px;font-size:13px;line-height:1.05">Subject<br>Title</div>
  <div class="rule" style="left:13px;top:52px;width:10px"></div>
  <div class="copy" style="left:13px;top:58px;width:58px">Lorem ipsum dolor sit amet, consectetuer adipiscing elit, sed diam nonummy nibh euismod tincidunt ut laoreet dolore magna aliquam erat volutpat. Ut wisi enim ad minim veniam, quis nostrud exerci tation ullamcorper suscipit lobortis nisl ut aliquip ex ea commodo consequat. Duis autem vel eum iriure.</div>
  <div class="bg-blue" style="left:114px;top:33px;width:156px;height:90px"></div>
  <div class="photo green" role="img" aria-label="Two tennis players smiling on court holding rackets" style="left:78px;top:0;width:52px;height:100px"></div>
  <div class="photo green" role="img" aria-label="Family walking on a green lawn by the coast" style="left:141px;top:52px;width:53px;height:87px"></div>
  <div style="left:199px;top:52px;font:700 7px/1.15 Roboto,sans-serif;color:var(--orange)">Lorem Ipsum<br>Dolor Sit<br>Ametkeeper.</div>
  <div class="copy-white" style="left:199px;top:88px;width:62px">Lorem ipsum dolor sit amet, consectetuer adipiscing elit, sed diam nonummy nibh euismod tincidunt ut laoreet dolore magna</div>
  <div class="page-no">3</div>
</section>

<!-- 4 Numbered list with feature box -->
<section class="slide col1 row2">
  <div class="brand">The Heron</div>
  <div class="heading" style="left:9px;top:10px">Text Added Here</div>
  <div class="rule" style="left:9px;top:24px"></div>
  <div style="left:25px;top:37px;width:100px">
    <div class="num">01. <span style="font-size:4px">Aliquam Erat Volutpat</span></div><div class="copy" style="margin:1px 0 7px 12px">Lorem ipsum dolor sit amet, consectetuer adipiscing elit, sed diam nonummy</div>
    <div class="num">02. <span style="font-size:4px">Consectetuer Adipiscing Elit</span></div><div class="copy" style="margin:1px 0 7px 12px">Lorem ipsum dolor sit amet, consectetuer adipiscing elit, sed diam nonummy</div>
    <div class="num">03. <span style="font-size:4px">Duis Autem Vel Eum</span></div><div class="copy" style="margin:1px 0 7px 12px">Lorem ipsum dolor sit amet, consectetuer adipiscing elit, sed diam nonummy</div>
    <div class="num">04. <span style="font-size:4px">Aliquam Erat Volutpat</span></div><div class="copy" style="margin:1px 0 0 12px">Lorem ipsum dolor sit amet, consectetuer adipiscing elit, sed diam nonummy</div>
  </div>
  <div class="bg-blue" style="left:148px;top:37px;width:89px;height:92px"></div>
  <div style="left:138px;top:42px;width:95px">
    <div style="position:relative;height:28px"><span style="position:absolute;left:0;top:2px;width:20px;height:20px;border-radius:50%;background:var(--orange);border:2px solid #fff"></span><span style="position:absolute;left:25px;top:2px;font:600 5px Montserrat,sans-serif;color:#fff">Lorem ipsum</span><span class="copy-white" style="position:absolute;left:25px;top:9px;width:65px">Lorem ipsum dolor sit amet, cons ectetuer adipiscing elit</span></div>
    <div style="position:relative;height:28px"><span style="position:absolute;left:0;top:2px;width:20px;height:20px;border-radius:50%;background:var(--orange);border:2px solid #fff"></span><span style="position:absolute;left:25px;top:2px;font:600 5px Montserrat,sans-serif;color:#fff">Lorem ipsum</span><span class="copy-white" style="position:absolute;left:25px;top:9px;width:65px">Lorem ipsum dolor sit amet, cons ectetuer adipiscing elit</span></div>
    <div style="position:relative;height:28px"><span style="position:absolute;left:0;top:2px;width:20px;height:20px;border-radius:50%;background:var(--orange);border:2px solid #fff"></span><span style="position:absolute;left:25px;top:2px;font:600 5px Montserrat,sans-serif;color:#fff">Lorem ipsum</span><span class="copy-white" style="position:absolute;left:25px;top:9px;width:65px">Lorem ipsum dolor sit amet, cons ectetuer adipiscing elit</span></div>
  </div>
  <div class="page-no">4</div>
</section>

<!-- 5 Divider: company -->
<section class="slide col2 row2 bg-blue">
  <div class="photo" role="img" aria-label="Faint beach scene with waiter and loungers under blue tint" style="left:0;top:0;width:270px;height:152px;background:linear-gradient(135deg,#1a6aa3,#0f5a94 60%,#0c4f85)"></div>
  <div class="sq" style="left:6px;top:5px"></div>
  <div class="divider-title" style="left:114px;top:54px">About<br><b>Our <span style="color:var(--orange)">Company</span></b></div>
</section>

<!-- 6 Education -->
<section class="slide col3 row2">
  <div class="brand">The Heron</div>
  <div class="heading" style="left:9px;top:10px">Our Education</div>
  <div class="rule" style="left:9px;top:24px"></div>
  <svg style="left:0;top:0" width="270" height="152" viewBox="0 0 270 152">
    <g fill="none" stroke="#27313b" stroke-width="1">
      <rect x="45" y="39" width="45" height="62" rx="4"/>
      <rect x="108" y="39" width="45" height="62" rx="4"/>
      <rect x="171" y="39" width="45" height="62" rx="4"/>
    </g>
    <g fill="#fff" stroke="#27313b" stroke-width="1"><circle cx="90" cy="57" r="2"/><circle cx="108" cy="90" r="2"/><circle cx="153" cy="57" r="2"/><circle cx="171" cy="90" r="2"/></g>
    <g fill="none" stroke="#6fccea" stroke-width=".8"><circle cx="67.5" cy="53" r="3"/><rect x="127" y="51" width="7" height="5"/><path d="M190 57l4-4 3 2 4-4"/></g>
  </svg>
  <div class="center" style="left:45px;top:61px;width:45px;font:700 4px Montserrat,sans-serif;color:var(--sky)">IDEA</div>
  <div class="center" style="left:108px;top:61px;width:45px;font:700 4px Montserrat,sans-serif;color:var(--orange)">PROMOTION</div>
  <div class="center" style="left:171px;top:61px;width:45px;font:700 4px Montserrat,sans-serif;color:var(--sky)">GROWTH</div>
  <div class="copy center" style="left:49px;top:67px;width:37px;font-size:2.6px">Lorem ipsum dolor sit amet, consectetuer adipiscing elit, sed diam nonummy nibh euismod</div>
  <div class="copy center" style="left:112px;top:67px;width:37px;font-size:2.6px">Lorem ipsum dolor sit amet, consectetuer adipiscing elit, sed diam nonummy nibh euismod</div>
  <div class="copy center" style="left:175px;top:67px;width:37px;font-size:2.6px">Lorem ipsum dolor sit amet, consectetuer adipiscing elit, sed diam nonummy nibh euismod</div>
  <div class="copy center" style="left:28px;top:118px;width:214px">Lorem ipsum dolor sit amet, consectetuer adipiscing elit, sed diam nonummy nibh euismod tincidunt ut laoreet dolore magna aliquam erat volutpat. Ut wisi enim ad minim veniam, quis nostrud exerci tation ullamcorper.</div>
  <div class="page-no">5</div>
</section>

<!-- 7 About us -->
<section class="slide col1 row3">
  <div class="brand">The Heron</div>
  <div class="bg-blue" style="left:0;top:105px;width:68px;height:47px"></div>
  <div class="photo warm" role="img" aria-label="Guests dining at a restaurant table served by staff" style="left:19px;top:24px;width:85px;height:108px"></div>
  <div class="heading" style="left:115px;top:27px;font-size:11px">About Us</div>
  <div class="rule" style="left:115px;top:41px"></div>
  <div class="copy" style="left:115px;top:47px;width:140px">Lorem ipsum dolor sit amet, consectetuer adipiscing elit, sed diam nonummy nibh euismod tincidunt ut laoreet dolore magna aliquam erat volutpat. Ut wisi enim ad minim veniam, quis nostrud exerci tation.<br><br>Ex ea commodo consequat. Duis autem vel eum iriure dolor in hendrerit in vulputate velit esse molestie consequat, vel illum dolore eu feugiat nulla facilisis at vero eros et accumsan et iusto odio dignissim qui blandit praesent luptatum zzril delenit augue duis dolore te feugait nulla facilisi.</div>
  <div class="copy" style="left:120px;top:104px;width:130px;display:grid;grid-template-columns:1fr 1fr;gap:5px 8px">
    <span>▸ Lorem ipsum dolor sit amet, consectetuer adipiscing elit</span><span>▸ Lorem ipsum dolor sit amet, consectetuer adipiscing elit</span>
    <span>▹ Lorem ipsum dolor sit amet, consectetuer adipiscing elit</span><span>▹ Lorem ipsum dolor sit amet, consectetuer adipiscing elit</span>
  </div>
  <div class="page-no">6</div>
</section>

<!-- 8 Bar and ring charts -->
<section class="slide col2 row3">
  <div class="brand">The Heron</div>
  <div class="heading" style="left:9px;top:10px">Text Added Here</div>
  <div class="rule" style="left:9px;top:24px"></div>
  <div class="copy" style="left:9px;top:30px;width:105px">Lorem ipsum dolor sit amet, consectetuer adipiscing elit, sed diam nonummy nibh euismod tincidunt ut laoreet dolore magna aliquam erat volutpat. Ut wisi enim ad minim veniam, quis nostrud exerci tation ullamcorper suscipit lobortis.</div>
  <svg style="left:0;top:0" width="270" height="152" viewBox="0 0 270 152" font-family="Montserrat,sans-serif">
    <g font-size="4.2" fill="#27313b" text-anchor="end"><text x="27" y="76">50%</text><text x="27" y="86">40%</text><text x="27" y="96">30%</text><text x="27" y="106">20%</text><text x="27" y="116">10%</text></g>
    <path d="M30 70V125H104" stroke="#27313b" stroke-width=".8" fill="none"/>
    <rect x="40" y="75" width="7" height="50" fill="#0f5a94"/>
    <rect x="56" y="97" width="7" height="28" fill="#f47b20"/>
    <rect x="72" y="113" width="7" height="12" fill="#0f5a94"/>
    <rect x="88" y="121" width="7" height="4" fill="#f47b20"/>
    <g font-size="4.5" fill="#27313b" text-anchor="middle"><text x="45" y="133">1980</text><text x="60" y="133">1990</text><text x="75" y="133">2000</text><text x="91" y="133">2010</text></g>
    <g fill="none" stroke-linecap="round" transform="rotate(-90 183 64)">
      <circle cx="183" cy="64" r="44" stroke="#dfe3e7" stroke-width="1" stroke-dasharray="1 1.5"/>
      <circle cx="183" cy="64" r="44" stroke="#0f5a94" stroke-width="2.2" stroke-dasharray="188 400"/>
      <circle cx="183" cy="64" r="38" stroke="#f47b20" stroke-width="2.2" stroke-dasharray="150 400"/>
      <circle cx="183" cy="64" r="32" stroke="#f47b20" stroke-width="1.4" stroke-dasharray="45 400"/>
      <circle cx="183" cy="64" r="32" stroke="#0f5a94" stroke-width="1.4" stroke-dasharray="0 50 90 400"/>
    </g>
    <text x="183" y="67" font-size="7" font-family="Roboto,sans-serif" font-weight="500" fill="#27313b" text-anchor="middle">Add Text</text>
    <g font-size="4" font-weight="700"><text x="137" y="46" fill="#0f5a94">68%</text><text x="151" y="84" fill="#f47b20">45%</text><text x="207" y="84" fill="#f47b20">15%</text><text x="178" y="95" fill="#0f5a94">35%</text></g>
    <circle cx="123" cy="121" r="1.8" fill="#0f5a94"/><circle cx="187" cy="121" r="1.8" fill="#0f5a94"/>
    <g font-size="3.8" fill="#27313b"><text x="127" y="122.5">Lorem ipsum</text><text x="191" y="122.5">Lorem ipsum</text></g>
  </svg>
  <div class="copy" style="left:127px;top:125px;width:50px;font-size:2.5px">Lorem ipsum dolor sit amet, consectetuer adipiscing elit, sed diam</div>
  <div class="copy" style="left:191px;top:125px;width:50px;font-size:2.5px">Lorem ipsum dolor sit amet, consectetuer adipiscing elit, sed diam</div>
  <div class="page-no">7</div>
</section>

<!-- 9 Market opportunities -->
<section class="slide col3 row3">
  <div class="brand">The Heron</div>
  <div class="heading" style="left:14px;top:17px;font-size:10px;line-height:1.1">Market<br>Opportunities.</div>
  <div class="bg-blue" style="left:0;top:48px;width:93px;height:75px"></div>
  <div class="copy-white" style="left:12px;top:53px;width:76px;font-size:4.2px;line-height:1.25">Lorem ipsum dolor sit amet, consectetuer adipiscing elit, sed diam nonummy nibh euismod tincidunt ut laoreet dolore magna aliquam erat volutpat. Ut wisi enim ad minim veniam, quis nostrud exerci tation ullamcorper suscipit lobortis nisl ut aliquip ex ea commodo consequat.</div>
  <div class="dot" style="left:34px;top:136px"></div><div class="dot" style="left:44px;top:136px;background:var(--orange)"></div><div class="dot" style="left:54px;top:136px"></div>
  <svg style="left:0;top:0" width="270" height="152" viewBox="0 0 270 152" font-family="Montserrat,sans-serif">
    <text x="112" y="26" font-size="4.3" fill="#27313b">CONSECTETUER ADIPISCING</text>
    <g stroke="#dfe3e7" stroke-width=".5"><path d="M112 34H250M112 44.7H250M112 55.3H250M112 66H250M112 76.7H250M112 87.3H250"/><path d="M250 34V98"/></g>
    <path d="M112 98H250M112 34V98" stroke="#27313b" stroke-width=".6"/>
    <g font-size="4.2" fill="#27313b" text-anchor="end"><text x="109" y="36">60</text><text x="109" y="46">50</text><text x="109" y="57">40</text><text x="109" y="67">30</text><text x="109" y="78">20</text><text x="109" y="88">10</text><text x="109" y="99">0</text></g>
    <rect x="121" y="40" width="14" height="58" fill="#0f5a94"/>
    <rect x="149" y="64" width="14" height="34" fill="#f47b20"/>
    <rect x="177" y="48" width="14" height="50" fill="#0f5a94"/>
    <rect x="205" y="68" width="14" height="30" fill="#f47b20"/>
    <g font-size="4.2" fill="#27313b" text-anchor="middle"><text x="128" y="106">JAN</text><text x="156" y="106">FEB</text><text x="184" y="106">MAR</text><text x="212" y="106">APR</text></g>
    <circle cx="111" cy="117" r="1.8" fill="#0f5a94"/><circle cx="186" cy="117" r="1.8" fill="#0f5a94"/>
    <g font-size="4.3" fill="#0f5a94" font-weight="600"><text x="115" y="118.5">Lorem Ipsum</text><text x="190" y="118.5">Lorem Ipsum</text></g>
  </svg>
  <div class="copy" style="left:115px;top:121px;width:62px;font-size:2.6px">Lorem ipsum dolor sit amet, consectetuer adipiscing elit, sed diam nonummy</div>
  <div class="copy" style="left:190px;top:121px;width:62px;font-size:2.6px">Lorem ipsum dolor sit amet, consectetuer adipiscing elit, sed diam nonummy</div>
  <div class="page-no">8</div>
</section>

<!-- 10 Divider: service -->
<section class="slide col1 row4 bg-orange">
  <div class="photo" role="img" aria-label="Faint beach scene with waiter and umbrellas under orange tint" style="left:0;top:0;width:270px;height:152px;background:linear-gradient(135deg,#f58a36,#f47b20 60%,#e8701a)"></div>
  <div class="sq blue" style="left:6px;top:5px"></div>
  <div class="divider-title" style="left:115px;top:55px">About<br><b>Our <span style="color:var(--blue)">Service</span></b></div>
</section>

<!-- 11 Values -->
<section class="slide col2 row4">
  <div class="brand">The Heron</div>
  <div style="left:16px;top:26px;font:400 11.5px/1.45 Roboto,sans-serif;color:var(--blue)">Lorem Ipsum<br>Dolor Sit<br>Ametkeeper.</div>
  <div class="bg-blue" style="left:0;top:82px;width:106px;height:47px"></div>
  <div class="copy-white" style="left:16px;top:86px;width:85px">Lorem ipsum dolor sit amet, consectetuer adipiscing elit, sed diam nonummy nibh euismod tincidunt erat volutpat.<br><br>Ut wisi enim ad minim veniam, quis nostrud exerci tation ullamcorper suscipit lobortis nisl ut aliquip ex ea commodo consequat.</div>
  <div class="icon-box bg-orange" style="left:121px;top:30px"><svg viewBox="0 0 12 12" fill="#fff"><circle cx="4" cy="4" r="1.8"/><circle cx="8" cy="4" r="1.8"/><path d="M1 10c0-3 6-3 6 0zM5 10c0-3 6-3 6 0z"/></svg></div>
  <div class="icon-box bg-orange" style="left:121px;top:68px"><svg viewBox="0 0 12 12" fill="#fff"><circle cx="4" cy="2.5" r="1.5"/><circle cx="8" cy="2.5" r="1.5"/><rect x="2.5" y="4.5" width="3" height="7"/><rect x="6.5" y="4.5" width="3" height="7"/></svg></div>
  <div class="icon-box bg-orange" style="left:121px;top:108px"><svg viewBox="0 0 12 12" fill="#fff"><path d="M6 8.5L2.5 5a2 2 0 0 1 3.5-2 2 2 0 0 1 3.5 2z"/><rect x="1" y="9.5" width="10" height="1.5"/></svg></div>
  <div style="left:150px;top:30px;width:105px"><div class="label" style="font-size:5px">We Before Me</div><div class="copy" style="margin-top:2px">Ipsum dolor sit amet, cons ectetuer adipiscing elit, sed diam nonummy nibh euismod tincidunt ut laoreet</div></div>
  <div style="left:150px;top:68px;width:105px"><div class="label" style="font-size:5px">We Are Good People</div><div class="copy" style="margin-top:2px">Ipsum dolor sit amet, cons ectetuer adipiscing elit, sed diam nonummy nibh euismod tincidunt ut laoreet dolore magna aliquam erat volutpat.</div></div>
  <div style="left:150px;top:108px;width:105px"><div class="label" style="font-size:5px">We Work with Heart</div><div class="copy" style="margin-top:2px">Ipsum dolor sit amet, cons ectetuer adipiscing elit, sed diam nonummy nibh euismod tincidunt</div></div>
  <div class="page-no">9</div>
</section>

<!-- 12 Maturity table -->
<section class="slide col3 row4">
  <div class="brand">The Heron</div>
  <div class="heading" style="left:9px;top:10px">Text Added Here</div>
  <div class="rule" style="left:9px;top:24px"></div>
  <div style="left:25px;top:38px;width:220px;display:grid;grid-template-columns:repeat(5,1fr);gap:3px">
    <div style="border:.6px solid var(--blue);height:70px"><div class="bg-blue center" style="color:#fff;font:700 3px/6px Montserrat,sans-serif">NAIVE</div><div class="copy center" style="padding:3px;font-size:2.5px">Lorem ipsum dolor sit amet, consectetuer adipiscing elit lorem dolor</div></div>
    <div style="border:.6px solid var(--orange);height:70px"><div class="bg-orange center" style="color:#fff;font:700 3px/6px Montserrat,sans-serif">AWARE</div><div class="copy center" style="padding:3px;font-size:2.5px">Lorem ipsum dolor sit amet, consectetuer adipiscing elit lorem dolor</div></div>
    <div style="border:.6px solid var(--blue);height:70px"><div class="bg-blue center" style="color:#fff;font:700 3px/6px Montserrat,sans-serif">DEFINED</div><div class="copy center" style="padding:3px;font-size:2.5px">Lorem ipsum dolor sit amet, consectetuer adipiscing elit lorem dolor</div></div>
    <div style="border:.6px solid var(--orange);height:70px"><div class="bg-orange center" style="color:#fff;font:700 3px/6px Montserrat,sans-serif">MANAGED</div><div class="copy center" style="padding:3px;font-size:2.5px">Lorem ipsum dolor sit amet, consectetuer adipiscing elit lorem dolor</div></div>
    <div style="border:.6px solid var(--blue);height:70px"><div class="bg-blue center" style="color:#fff;font:700 3px/6px Montserrat,sans-serif">MANAGED</div><div class="copy center" style="padding:3px;font-size:2.5px;color:var(--ink)">Lorem ipsum dolor sit amet, consectetuer adipiscing elit lorem dolor</div></div>
  </div>
  <div style="left:25px;top:123px;width:220px;height:5px;display:grid;grid-template-columns:repeat(6,1fr);font:700 2.2px/5px Montserrat,sans-serif;color:#fff;text-align:center">
    <span class="bg-blue">ESTABLISH CONTEXT</span><span class="bg-orange">IDENTIFY RISK</span><span class="bg-blue">ANALYZE RISK</span><span class="bg-orange">EVALUATE RISK</span><span class="bg-blue">TREAT RISK</span><span class="bg-blue">MONITOR AND REVIEW</span>
  </div>
  <div class="page-no">10</div>
</section>

<!-- 13 Numbered points with photo -->
<section class="slide col1 row5">
  <div class="brand">The Heron</div>
  <div class="heading" style="left:29px;top:12px">Text Added Here</div>
  <div class="bg-orange" style="left:40px;top:28px;width:34px;height:2px"></div>
  <div class="photo" role="img" aria-label="Covered veranda with wooden dining table overlooking the sea" style="left:18px;top:30px;width:90px;height:105px;background:linear-gradient(160deg,#e8e3d8,#b9a58a 55%,#5e4a38)"></div>
  <div class="bg-orange" style="left:122px;top:40px;width:14px;height:14px;border-radius:50%;color:#fff;font:700 6px/14px Montserrat,sans-serif;text-align:center">1</div>
  <div class="bg-blue" style="left:122px;top:73px;width:14px;height:14px;border-radius:50%;color:#fff;font:700 6px/14px Montserrat,sans-serif;text-align:center">2</div>
  <div class="bg-orange" style="left:122px;top:107px;width:14px;height:14px;border-radius:50%;color:#fff;font:700 6px/14px Montserrat,sans-serif;text-align:center">3</div>
  <div class="copy" style="left:143px;top:41px;width:100px">Lorem ipsum dolor sit amet, consectetuer adipiscing elit, sed diam nonummy nibh euismod tincidunt ut laoreet dolore magna aliquam erat volutpat.</div>
  <div class="copy" style="left:143px;top:74px;width:100px">Ullamcorper suscipit lobortis nisl ut aliquip ex ea commodo consequat. Duis autem vel eum iriure dolor.<br><br>Molestie consequat, vel illum dolore eu feugiat nulla</div>
  <div class="copy" style="left:143px;top:108px;width:100px">Lorem ipsum dolor sit amet, consectetuer adipiscing elit, sed diam nonummy nibh euismod tincidunt ut laoreet dolore magna aliquam erat volutpat.</div>
  <div class="page-no">11</div>
</section>

<!-- 14 Icon grid -->
<section class="slide col2 row5">
  <div class="brand">The Heron</div>
  <div class="heading" style="left:11px;top:7px">Text Added Here</div>
  <div class="rule" style="left:11px;top:21px"></div>
  <div style="left:20px;top:32px;width:232px;display:grid;grid-template-columns:repeat(3,1fr);row-gap:10px;text-align:center">
    <div><div class="icon-box bg-blue" style="position:relative;margin:0 auto"><svg viewBox="0 0 12 12" fill="none" stroke="#fff" stroke-width=".8"><circle cx="4" cy="4" r="1.6"/><circle cx="8" cy="4" r="1.6"/><path d="M1.5 10c0-3 5-3 5 0M5.5 10c0-3 5-3 5 0"/></svg></div><div class="label" style="color:var(--ink);margin-top:4px">Lorem ipsum</div><div class="copy" style="width:50px;margin:1px auto 0">Lorem ipsum dolor sit amet, consectetuer adipiscing elit</div></div>
    <div><div class="icon-box bg-orange" style="position:relative;margin:0 auto"><svg viewBox="0 0 12 12" fill="none" stroke="#fff" stroke-width=".8"><circle cx="5" cy="5" r="3"/><circle cx="9" cy="3" r="1.5"/><path d="M3 10h6"/></svg></div><div class="label" style="color:var(--ink);margin-top:4px">Lorem ipsum</div><div class="copy" style="width:50px;margin:1px auto 0">Lorem ipsum dolor sit amet, consectetuer adipiscing elit</div></div>
    <div><div class="icon-box bg-blue" style="position:relative;margin:0 auto"><svg viewBox="0 0 12 12" fill="none" stroke="#fff" stroke-width=".8"><rect x="2" y="6" width="2" height="4"/><rect x="5" y="4" width="2" height="6"/><rect x="8" y="2" width="2" height="8"/></svg></div><div class="label" style="color:var(--ink);margin-top:4px">Lorem ipsum</div><div class="copy" style="width:50px;margin:1px auto 0">Lorem ipsum dolor sit amet, consectetuer adipiscing elit</div></div>
    <div><div class="icon-box bg-orange" style="position:relative;margin:0 auto"><svg viewBox="0 0 12 12" fill="none" stroke="#fff" stroke-width=".8"><path d="M2 2v8h8M3 3c1 4 3 6 7 6"/></svg></div><div class="label" style="color:var(--ink);margin-top:4px">Lorem ipsum</div><div class="copy" style="width:50px;margin:1px auto 0">Lorem ipsum dolor sit amet, consectetuer adipiscing elit</div></div>
    <div><div class="icon-box bg-blue" style="position:relative;margin:0 auto"><svg viewBox="0 0 12 12" fill="none" stroke="#fff" stroke-width=".8"><path d="M4 2h4l-1 2c3 1 3 6 0 6H5c-3 0-3-5 0-6z"/></svg></div><div class="label" style="color:var(--ink);margin-top:4px">Lorem ipsum</div><div class="copy" style="width:50px;margin:1px auto 0">Lorem ipsum dolor sit amet, consectetuer adipiscing elit</div></div>
    <div><div class="icon-box bg-orange" style="position:relative;margin:0 auto"><svg viewBox="0 0 12 12" fill="none" stroke="#fff" stroke-width=".8"><circle cx="6" cy="5" r="3"/><path d="M4 8l-1 3 3-1 3 1-1-3"/></svg></div><div class="label" style="color:var(--ink);margin-top:4px">Lorem ipsum</div><div class="copy" style="width:50px;margin:1px auto 0">Lorem ipsum dolor sit amet, consectetuer adipiscing elit</div></div>
  </div>
  <div class="page-no">12</div>
</section>

<!-- 15 Divider: project -->
<section class="slide col3 row5 bg-blue">
  <div class="photo" role="img" aria-label="Faint beach scene with umbrellas under blue tint" style="left:0;top:0;width:270px;height:152px;background:linear-gradient(135deg,#1a6aa3,#0f5a94 60%,#0c4f85)"></div>
  <div class="sq" style="left:6px;top:5px"></div>
  <div class="divider-title" style="left:115px;top:55px">About<br><b>Our <span style="color:var(--orange)">Project</span></b></div>
</section>

<!-- 16 Photo story -->
<section class="slide col1 row6">
  <div class="brand">The Heron</div>
  <div class="sq" style="left:10px;top:8px;width:14px;height:14px"></div>
  <div class="bg-blue" style="left:32px;top:135px;width:131px;height:17px"></div>
  <div class="photo warm" role="img" aria-label="Stone building with terracotta tiled roof against blue sky" style="left:15px;top:13px;width:62px;height:120px;background:linear-gradient(180deg,#7fb0d8,#b9a48a 45%,#a55a3a)"></div>
  <div class="heading center" style="left:95px;top:34px;width:164px;font-size:9px">Text Added Here</div>
  <div class="copy center" style="left:112px;top:46px;width:135px">Lorem ipsum dolor sit amet, consectetuer adipiscing elit, sed diam nonummy nibh euismod tincidunt erat volutpat. Ut wisi enim ad minim veniam, quis nostrud exerci tation ullamcorper suscipit<br><br>Lobortis nisl ut aliquip ex ea commodo consequat. Ut wisi enim ad minim veniam, quis nostrud exerci tation ullamcorper suscipit.</div>
  <div class="photo warm" role="img" aria-label="Group of friends laughing together outdoors" style="left:103px;top:86px;width:150px;height:48px"></div>
  <div class="page-no">13</div>
</section>

<!-- 17 Cycle diagram -->
<section class="slide col2 row6">
  <div class="brand">The Heron</div>
  <div class="heading" style="left:10px;top:7px">Text Added Here</div>
  <div class="rule" style="left:10px;top:21px"></div>
  <div class="copy" style="left:10px;top:27px;width:82px">Lorem ipsum dolor sit amet, consectetuer adipiscing elit, sed diam nonummy nibh.<br><br>Ut wisi enim ad minim veniam, quis nostrud exerci tation ullamcorper suscipit lobortis. Ut wisi enim ad minim veniam, quis nostrud.</div>
  <div class="bg-orange" style="left:0;top:78px;width:83px;height:62px"></div>
  <div style="left:8px;top:82px;width:72px;font:600 4px Montserrat,sans-serif;color:#fff">
    <div>● Lorem ipsum</div><div class="copy-white" style="margin:1px 0 5px 5px;font-size:2.5px">Lorem ipsum dolor sit amet, consectetuer adipiscing elit</div>
    <div>● Lorem ipsum</div><div class="copy-white" style="margin:1px 0 5px 5px;font-size:2.5px">Lorem ipsum dolor sit amet, consectetuer adipiscing elit</div>
    <div>● Lorem ipsum</div><div class="copy-white" style="margin:1px 0 0 5px;font-size:2.5px">Lorem ipsum dolor sit amet, consectetuer adipiscing elit</div>
  </div>
  <svg style="left:0;top:0" width="270" height="152" viewBox="0 0 270 152" font-family="Montserrat,sans-serif">
    <path d="M132.5 94.4A42 42 0 1 1 151 116.4" fill="none" stroke="#27313b" stroke-width="2.2"/>
    <path d="M129 89l3.5 6 4-5" fill="none" stroke="#27313b" stroke-width="1.4"/>
    <circle cx="199" cy="48" r="11" fill="#0f5a94"/><circle cx="199" cy="48" r="6.5" fill="#fff"/><circle cx="199" cy="48" r="2.8" fill="none" stroke="#0f5a94" stroke-width="1"/>
    <circle cx="213" cy="91" r="8.5" fill="#f47b20"/><circle cx="213" cy="91" r="4.8" fill="#fff"/>
    <circle cx="190" cy="118" r="6.5" fill="#0f5a94"/><circle cx="190" cy="118" r="3.8" fill="#fff"/>
    <circle cx="151" cy="116" r="5.5" fill="#f47b20"/><circle cx="151" cy="116" r="3.2" fill="#fff"/>
    <rect x="166" y="64" width="2" height="7" fill="#f47b20"/><rect x="169" y="67" width="2" height="4" fill="#0f5a94"/><rect x="172" y="65" width="2" height="6" fill="#f47b20"/><rect x="175" y="66" width="2" height="5" fill="#0f5a94"/>
    <text x="172" y="79" font-size="4.5" fill="#27313b" text-anchor="middle">MAIN TITLE</text>
    <g font-size="2.5" fill="#8b949d" text-anchor="middle"><text x="172" y="84">Lorem ipsum dolor sit</text><text x="172" y="87.5">amet consectetuer</text></g>
    <g font-size="3.5" fill="#27313b"><text x="224" y="44">Your Title</text><text x="226" y="88">Your Title</text><text x="200" y="130">Your Title</text><text x="115" y="126">Your Title</text></g>
    <g font-size="3" fill="#f47b20"><text x="212" y="36">85%</text><text x="190" y="94">80%</text><text x="160" y="112">50%</text><text x="199" y="122">75%</text></g>
  </svg>
  <div class="page-no">14</div>
</section>

<!-- 18 Two columns -->
<section class="slide col3 row6">
  <div class="brand">The Heron</div>
  <div class="heading" style="left:9px;top:7px">Text Added Here</div>
  <div class="rule" style="left:9px;top:21px"></div>
  <div style="left:27px;top:29px;width:103px"><div class="label" style="font-size:5px">1. Text Added Here</div><div class="copy" style="margin-top:2px">Lorem ipsum dolor sit amet, cons ectetuer adipiscing elit, sed diam nonummy nibh euismod tincidunt ut laoreet dolore magna aliquam erat volutpat. Ut wisi enim ad minim veniam, quis nostrud exerci tation ullamcorper suscipit lobortis nisl ut aliquip ex ea commodo consequat.<br><br>Lorem ipsum dolor sit amet, consectetuer adipiscing elit, sed diam nonummy nibh euismod tincidunt ut laoreet dolore magna aliquam erat volutpat.</div></div>
  <div style="left:142px;top:29px;width:103px"><div class="label" style="font-size:5px">2. Text Added Here</div><div class="copy" style="margin-top:2px">Lorem ipsum dolor sit amet, cons ectetuer adipiscing elit, sed diam nonummy nibh euismod tincidunt ut laoreet dolore magna aliquam erat volutpat. Ut wisi enim ad minim veniam, quis nostrud exerci tation ullamcorper suscipit lobortis nisl ut aliquip ex ea commodo consequat.<br><br>Lorem ipsum dolor sit amet, consectetuer adipiscing elit, sed diam nonummy nibh euismod tincidunt ut laoreet dolore magna aliquam erat volutpat.</div></div>
  <div class="bg-orange" style="left:32px;top:93px;width:10px;height:10px;color:#fff;font:700 6px/10px Montserrat,sans-serif;text-align:center">1.</div>
  <div class="bg-orange" style="left:32px;top:117px;width:10px;height:10px;color:#fff;font:700 6px/10px Montserrat,sans-serif;text-align:center">2.</div>
  <div class="bg-orange" style="left:150px;top:93px;width:10px;height:10px;color:#fff;font:700 6px/10px Montserrat,sans-serif;text-align:center">1.</div>
  <div class="bg-orange" style="left:150px;top:117px;width:10px;height:10px;color:#fff;font:700 6px/10px Montserrat,sans-serif;text-align:center">2.</div>
  <div style="left:47px;top:92px;width:70px"><div class="label" style="color:var(--ink)">Lorem ipsum</div><div class="copy">Lorem ipsum dolor sit amet, consectetuer adipiscing elit, sed diam</div></div>
  <div style="left:47px;top:116px;width:70px"><div class="label" style="color:var(--ink)">Lorem ipsum</div><div class="copy">Lorem ipsum dolor sit amet, consectetuer adipiscing elit, sed diam</div></div>
  <div style="left:166px;top:92px;width:70px"><div class="label" style="color:var(--ink)">Lorem ipsum</div><div class="copy">Lorem ipsum dolor sit amet, consectetuer adipiscing elit, sed diam</div></div>
  <div style="left:166px;top:116px;width:70px"><div class="label" style="color:var(--ink)">Lorem ipsum</div><div class="copy">Lorem ipsum dolor sit amet, consectetuer adipiscing elit, sed diam</div></div>
  <div class="page-no">15</div>
</section>

<!-- 19 Timeline -->
<section class="slide col1 row7">
  <div class="brand">The Heron</div>
  <div class="heading" style="left:9px;top:10px">Text Added Here</div>
  <div class="rule" style="left:9px;top:24px"></div>
  <svg style="left:0;top:0" width="270" height="152" viewBox="0 0 270 152" font-family="Roboto,sans-serif">
    <g fill="none" stroke="#0f5a94" stroke-width="1.2">
      <path d="M35 80V58q0-6 6-6h27q6 0 6 6v22"/>
      <path d="M110 80V58q0-6 6-6h27q6 0 6 6v22"/>
      <path d="M185 80V58q0-6 6-6h27q6 0 6 6v22"/>
      <path d="M30 80H230"/>
      <path d="M74 80v22q0 6 6 6h24q6 0 6-6V80"/>
      <path d="M149 80v22q0 6 6 6h24q6 0 6-6V80"/>
    </g>
    <g fill="#fff" stroke="#0f5a94" stroke-width="1.5"><circle cx="54.5" cy="52" r="5"/><circle cx="129.5" cy="52" r="5"/><circle cx="204.5" cy="52" r="5"/></g>
    <g fill="#fff" stroke="#f47b20" stroke-width="1.5"><circle cx="92" cy="108" r="5"/><circle cx="167" cy="108" r="5"/></g>
    <g font-size="8" font-weight="500" text-anchor="middle"><text x="54.5" y="73" fill="#f47b20">2018</text><text x="129.5" y="73" fill="#f47b20">2020</text><text x="204.5" y="73" fill="#f47b20">2022</text><text x="92" y="96" fill="#0f5a94">2019</text><text x="167" y="96" fill="#0f5a94">2021</text></g>
    <g fill="#f47b20"><rect x="88" y="34" width="2" height="4"/><rect x="91" y="32" width="2" height="6"/><rect x="163" y="31" width="6" height="6" rx="1"/><circle cx="54.5" cy="93" r="2.5"/><circle cx="129.5" cy="92" r="2.5"/></g>
    <text x="204" y="96" font-size="5" fill="#0f5a94" text-anchor="middle">$</text>
  </svg>
  <div class="center" style="left:76px;top:42px;width:32px"><div style="font:700 3px Montserrat,sans-serif;color:var(--ink)">LOREM IPSUM</div><div class="copy" style="font-size:2.6px">Lorem ipsum dolor sit amet, consectetuer adipiscing elit</div></div>
  <div class="center" style="left:151px;top:42px;width:32px"><div style="font:700 3px Montserrat,sans-serif;color:var(--ink)">LOREM IPSUM</div><div class="copy" style="font-size:2.6px">Lorem ipsum dolor sit amet, consectetuer adipiscing elit</div></div>
  <div class="center" style="left:38px;top:98px;width:32px"><div style="font:700 3px Montserrat,sans-serif;color:var(--ink)">LOREM IPSUM</div><div class="copy" style="font-size:2.6px">Lorem ipsum dolor sit amet, consectetuer adipiscing elit</div></div>
  <div class="center" style="left:113px;top:98px;width:32px"><div style="font:700 3px Montserrat,sans-serif;color:var(--ink)">LOREM IPSUM</div><div class="copy" style="font-size:2.6px">Lorem ipsum dolor sit amet, consectetuer adipiscing elit</div></div>
  <div class="center" style="left:188px;top:98px;width:32px"><div style="font:700 3px Montserrat,sans-serif;color:var(--ink)">LOREM IPSUM</div><div class="copy" style="font-size:2.6px">Lorem ipsum dolor sit amet, consectetuer adipiscing elit</div></div>
  <div class="page-no">16</div>
</section>

<!-- 20 Team -->
<section class="slide col2 row7">
  <div class="brand">The Heron</div>
  <div class="heading" style="left:16px;top:10px">Our Team</div>
  <div class="rule" style="left:16px;top:24px"></div>
  <div class="copy" style="left:16px;top:29px;width:238px">Lorem ipsum dolor sit amet, consectetuer adipiscing elit, sed diam nonummy nibh euismod tincidunt ut laoreet dolore magna aliquam erat volutpat. Ut wisi enim ad minim veniam, quis nostrud exerci tation ullamcorper suscipit lobortis nisl ut aliquip ex ea commodo consequat. Duis autem vel eum iriure dolor in hendrerit in vulputate velit esse molestie consequat.<br><br>Lorem ipsum dolor sit amet, cons ectetuer adipiscing elit, sed diam nonummy nibh euismod tincidunt ut laoreet dolore magna aliquam erat volutpat.</div>
  <div class="bg-blue" style="left:0;top:82px;width:270px;height:48px"></div>
  <div style="left:22px;top:70px;width:226px;display:grid;grid-template-columns:repeat(4,1fr);gap:8px;text-align:center">
    <div><div role="img" aria-label="Team member portrait" style="width:22px;height:22px;margin:0 auto;border-radius:50%;border:1.5px solid var(--orange);background:#c9b7a6"></div><div style="font:700 4px Montserrat,sans-serif;color:var(--orange);margin-top:2px">JOHN SMITH</div><div class="copy-white" style="font-size:2.5px">Lorem ipsum dolor sit amet, cons ectetuer adipiscing elit, sed diam nonummy</div></div>
    <div><div role="img" aria-label="Team member portrait" style="width:22px;height:22px;margin:0 auto;border-radius:50%;border:1.5px solid var(--orange);background:#a98a76"></div><div style="font:700 4px Montserrat,sans-serif;color:var(--orange);margin-top:2px">MILLIE SMITH</div><div class="copy-white" style="font-size:2.5px">Lorem ipsum dolor sit amet, cons ectetuer adipiscing elit, sed diam nonummy</div></div>
    <div><div role="img" aria-label="Team member portrait" style="width:22px;height:22px;margin:0 auto;border-radius:50%;border:1.5px solid var(--orange);background:#c9b7a6"></div><div style="font:700 4px Montserrat,sans-serif;color:var(--orange);margin-top:2px">JOHN SMITH</div><div class="copy-white" style="font-size:2.5px">Lorem ipsum dolor sit amet, cons ectetuer adipiscing elit, sed diam nonummy</div></div>
    <div><div role="img" aria-label="Team member portrait" style="width:22px;height:22px;margin:0 auto;border-radius:50%;border:1.5px solid var(--orange);background:#a98a76"></div><div style="font:700 4px Montserrat,sans-serif;color:var(--orange);margin-top:2px">MILLIE SMITH</div><div class="copy-white" style="font-size:2.5px">Lorem ipsum dolor sit amet, cons ectetuer adipiscing elit, sed diam nonummy</div></div>
  </div>
  <div class="page-no">16</div>
</section>

<!-- 21 Thank you -->
<section class="slide col3 row7">
  <div class="center" style="left:0;top:20px;width:270px;color:var(--blue);font:500 18px/1 Roboto,sans-serif">The Heron</div>
  <div style="left:40px;top:66px;font:700 26px/1.05 Roboto,sans-serif;color:#33373b;text-align:right;width:70px">Thank<br>You</div>
  <div class="photo pool" role="img" aria-label="Woman relaxing on a lounger beside the pool" style="left:124px;top:61px;width:90px;height:69px"></div>
  <div class="bg-orange" style="left:216px;top:61px;width:14px;height:69px"></div>
  <div style="left:223px;top:96px;transform:translate(-50%,-50%) rotate(-90deg);white-space:nowrap;font:500 4.5px Montserrat,sans-serif;color:#fff;letter-spacing:.5px">www.website.com</div>
  <div class="sq blue" style="left:9px;top:137px;width:8px;height:8px"></div>
</section>

</body>
</html>
```